Vela Stewardship Business Card design

We need a creative business card design for our hospitality management company
We need the following information:
Our business Logo: Vela Stewardship
Name: Mara Dobrinsky
Phone number: 0458 317 642
Email: mara@velastewardship.com.au
Address: 214/53 Penrose Street, South Melbourne 3206
Web: www.velastewardship.com.au
I need the design to be a working file so that I can insert the names and numbers of the other staff members of our business.
The cards need to be 90 x 40mm
Thanks
Industry/Entity Type
Hospitality
Look and feel

```html
<!DOCTYPE html>
<html lang="en">
<head>
<meta charset="utf-8">
<title>Vela Stewardship Business Card</title>
<link rel="stylesheet" href="https://fonts.googleapis.com/css2?family=Arimo:wght@400;700&display=swap">
<style>
  :root {
    --backdrop: #d9dadc;
    --card: #ffffff;
    --navy: #1d3f6e;
    --brand-blue: #1f5fa8;
    --link-blue: #2a8fd6;
    --ink: #222222;
    --ink-soft: #3a3a3a;
  }
  * { box-sizing: border-box; margin: 0; padding: 0; }
  html, body {
    width: 1200px; height: 951px; overflow: hidden;
    background: var(--backdrop);
    font-family: "Arimo", Arial, sans-serif;
    color: var(--ink);
  }
  .card {
    position: absolute;
    left: 220px;
    width: 760px; height: 338px;
    background: var(--card);
    border-radius: 22px;
    overflow: hidden;
    box-shadow: 0 6px 18px rgba(0,0,0,0.18);
  }
  .card--front { top: 107px; }
  .card--back { top: 505px; }

  .brand {
    display: flex; align-items: center; justify-content: center; gap: 16px;
  }
  .brand__mark {
    background: var(--brand-blue);
  }
  .brand__name {
    font-weight: 700;
    color: var(--brand-blue);
    text-transform: uppercase;
    letter-spacing: 0.5px;
  }

  .card--front .brand {
    position: absolute; top: 118px; left: 0; right: 0;
  }
  .card--front .brand__mark { width: 34px; height: 34px; }
  .card--front .brand__name { font-size: 44px; }
  .front__web {
    position: absolute; top: 200px; left: 0; right: 0;
    text-align: center;
    font-size: 20px; letter-spacing: 2.5px;
    color: var(--ink-soft);
  }

  .back__edge {
    position: absolute; top: 0; right: 0; bottom: 0; width: 18px;
    background: var(--navy);
  }
  .card--back .brand {
    position: absolute; top: 92px; left: 330px; justify-content: flex-start;
  }
  .card--back .brand__mark { width: 26px; height: 26px; }
  .card--back .brand__name { font-size: 34px; color: var(--navy); }

  .name-bar {
    position: absolute; top: 172px; left: 0; width: 392px; height: 40px;
    background: var(--navy);
    color: #fff;
    display: flex; align-items: center; gap: 12px;
    padding-left: 26px;
    font-size: 21px; letter-spacing: 0.5px;
  }
  .name-bar__role { font-size: 17px; }

  .contact {
    position: absolute; font-size: 18px; line-height: 26px; color: var(--ink);
  }
  .contact--address { top: 240px; left: 34px; }
  .contact--lines { top: 238px; left: 372px; }
  .contact__row { display: flex; align-items: flex-start; gap: 10px; }
  .contact__icon { width: 16px; height: 16px; margin-top: 4px; flex: none; }
  .contact__indent { padding-left: 26px; }
  .contact__domain { color: var(--link-blue); }
</style>
</head>
<body>

<section class="card card--front" aria-label="Card front">
  <div class="brand">
    <span class="brand__mark"></span>
    <span class="brand__name">Vela Stewardship</span>
  </div>
  <p class="front__web">www.velastewardship.com.au</p>
</section>

<section class="card card--back" aria-label="Card back">
  <div class="back__edge"></div>
  <div class="brand">
    <span class="brand__mark"></span>
    <span class="brand__name">Vela Stewardship</span>
  </div>

  <div class="name-bar">
    <span class="name-bar__name">Mara Dobrinsky</span>
    <span class="name-bar__role">Manager</span>
  </div>

  <div class="contact contact--address">
    <div class="contact__row">
      <svg class="contact__icon" viewBox="0 0 16 16" aria-hidden="true">
        <path d="M8 1 L15 7.5 H13 V15 H9.5 V10.5 H6.5 V15 H3 V7.5 H1 Z" fill="#2a8fd6"/>
      </svg>
      <span>214/53 Penrose Street</span>
    </div>
    <div class="contact__indent">South Melbourne 3206</div>
  </div>

  <div class="contact contact--lines">
    <div class="contact__row">
      <svg class="contact__icon" viewBox="0 0 16 16" aria-hidden="true">
        <path d="M4 1.5 L6.5 4.5 L5 6.5 C6 8.5 7.5 10 9.5 11 L11.5 9.5 L14.5 12 L12.5 14.5 C7 14 2 9 1.5 3.5 Z" fill="#2a8fd6"/>
      </svg>
      <span>0458 317 642</span>
    </div>
    <div class="contact__row">
      <svg class="contact__icon" viewBox="0 0 16 16" aria-hidden="true">
        <rect x="1" y="3.5" width="14" height="9.5" rx="1" fill="#2a8fd6"/>
        <path d="M1.5 4.2 L8 9 L14.5 4.2" fill="none" stroke="#fff" stroke-width="1.3"/>
      </svg>
      <span>mara@velastewardship.com.au</span>
    </div>
    <div class="contact__row">
      <svg class="contact__icon" viewBox="0 0 16 16" aria-hidden="true">
        <circle cx="8" cy="8" r="7" fill="#2a8fd6"/>
      </svg>
      <span>www.<span class="contact__domain">velastewardship</span>.com.au</span>
    </div>
  </div>
</section>

</body>
</html>
```